Etiketten-Design für Himbeer-Gin
Zielgruppe
GIN
Aufgabenstellung
Wir benötigen ein Etikett für unseren neuen Himbeere GIN, der Name des GINs lautet: KorvalaGIN und soll für folgende Flasche dargestellt werden: https://www.flakoria-beispiel.de/luma-flasche-500ml-schwarz-beschichtet-tqx41-karton-48stk.html
mit dem Etikett https://klebmarken-beispiel.de/anwendungen/fluoreszierende-etiketten/ Himbeerlastiges Design mit bestehendem Logo (WendelGIN) siehe Daten. Bei Fragen stehe ich gerne zur Verfügung!

```html
<!DOCTYPE html>
<html lang="de">
<head>
<meta charset="utf-8">
<title>KorvalaGIN – Etikett</title>
<link rel="stylesheet" href="https://fonts.googleapis.com/css2?family=Marcellus&family=Ubuntu:wght@400;700&display=swap">
<style>
  :root {
    --page-bg: #d9d9d9;
    --label-bg: #1a1b1d;
    --raspberry: #e4007f;
    --gold: #b8931a;
    --leaf-line: #3a3b3e;
  }
  * { margin: 0; padding: 0; box-sizing: border-box; }
  html, body {
    width: 1200px;
    height: 1062px;
    overflow: hidden;
    background: var(--page-bg);
  }
  .canvas {
    position: relative;
    width: 1200px;
    height: 1062px;
  }
  .label {
    position: absolute;
    left: 315px;
    top: 24px;
    width: 570px;
    height: 1015px;
    background: var(--label-bg);
    border-radius: 22px;
    color: var(--gold);
  }
  .label__name {
    position: absolute;
    top: 92px;
    left: 0;
    width: 100%;
    text-align: center;
    font-family: "Marcellus", serif;
    font-weight: 400;
    font-size: 104px;
    line-height: 1;
    color: var(--raspberry);
  }
  .label__category {
    position: absolute;
    top: 202px;
    left: 0;
    width: 100%;
    text-align: center;
    font-family: "Marcellus", serif;
    font-size: 136px;
    line-height: 1;
    color: var(--gold);
  }
  .label__artwork {
    position: absolute;
    left: 60px;
    top: 345px;
    width: 450px;
    height: 420px;
    display: block;
  }
  .label__origin {
    position: absolute;
    top: 780px;
    left: 0;
    width: 100%;
    text-align: center;
    font-family: "Marcellus", serif;
    font-size: 33px;
    letter-spacing: 1px;
    line-height: 1;
  }
  .label__style {
    position: absolute;
    top: 820px;
    left: 0;
    width: 100%;
    text-align: center;
    font-family: "Ubuntu", sans-serif;
    font-weight: 700;
    font-size: 25px;
    letter-spacing: 1px;
    line-height: 1;
  }
  .label__volume {
    position: absolute;
    left: 130px;
    top: 876px;
    font-family: "Ubuntu", sans-serif;
    font-size: 30px;
    line-height: 1;
    color: var(--gold);
  }
  .label__abv {
    position: absolute;
    right: 148px;
    top: 876px;
    font-family: "Ubuntu", sans-serif;
    font-size: 30px;
    line-height: 1.1;
    text-align: right;
    color: var(--raspberry);
  }
</style>
</head>
<body>
<main class="canvas">
  <section class="label">
    <h1 class="label__name">Korvala</h1>
    <p class="label__category">GIN</p>

    <svg class="label__artwork" viewBox="0 0 450 420" role="img"
         aria-label="Illustration: zwei pinke Himbeeren mit weiß gezeichneten Blättern und Stiel">
      <defs>
        <linearGradient id="berryTone" x1="0" y1="0" x2="0" y2="1">
          <stop offset="0%" stop-color="#2a2b2e"/>
          <stop offset="45%" stop-color="#3a2a33"/>
          <stop offset="70%" stop-color="#b8006a"/>
          <stop offset="100%" stop-color="#e4007f"/>
        </linearGradient>
      </defs>
      <rect width="450" height="420" rx="28" fill="url(#berryTone)"/>
    </svg>

    <p class="label__origin">SCHWÄBISCHER</p>
    <p class="label__style">DRY GIN</p>
    <p class="label__volume">0,5l</p>
    <p class="label__abv">43%<br>Vol</p>
  </section>
</main>
</body>
</html>
```